Business Card Design Project

Industry/Entity Type

Business

Contact Information for Business Card

The Harlow Vale Gospel Choir
Dean Marsell, Minister of Music

The Coastal Wesleyan Church of Bramford Hill
Founded 1792

Twitter @thehvgc
Instagram harlowvalegc
Facebook facebook.com/hvgc408
Website: harlowvalegc-example.org
For Bookings: (555) 204-HVGC
4287 Bramwell Street, Philadelphia, PA 19874

Back of the Card
Music and Cd's Recordings Available On
Choirs Website and Also
Tunevox, Orbala Sound, Disc Sprout (the music online logo)

```html
<!DOCTYPE html>
<html lang="en">
<head>
<meta charset="utf-8">
<title>Harlow Vale Gospel Choir – Business Card</title>
<link rel="stylesheet" href="https://fonts.googleapis.com/css2?family=Roboto:wght@400;500&family=Roboto+Condensed:wght@400;700&family=Italianno&display=swap">
<style>
  :root {
    --backdrop: #2a2a2a;
    --card-blue: #1d65a6;
    --card-white: #f1f1f1;
    --brand-red: #c8272e;
    --brand-blue: #1d5fa8;
    --text-grey: #555555;
    --rule-grey: #9a9a9a;
    --white: #ffffff;
    --crest-dark: #3a3a3a;
  }
  * { margin: 0; padding: 0; box-sizing: border-box; }
  html, body { width: 1200px; height: 960px; overflow: hidden; background: var(--backdrop); }
  .canvas { position: relative; width: 1200px; height: 960px; }

  .card { position: absolute; left: 320px; width: 600px; border-radius: 20px; overflow: hidden; }

  /* Back of card */
  .card-back { top: 108px; height: 342px; background: var(--card-blue); color: var(--white); text-align: center; }
  .back-crest {
    position: absolute; left: 240px; top: 62px; width: 120px; height: 130px;
    display: flex; align-items: center; justify-content: center;
    font-family: "Roboto Condensed", sans-serif; font-weight: 700; font-size: 28px; letter-spacing: 2px;
    color: var(--white);
  }
  .back-tagline {
    position: absolute; left: 0; right: 0; top: 206px;
    font-family: "Italianno", cursive; font-size: 30px; line-height: 27px;
  }
  .store-list {
    position: absolute; left: 0; right: 0; top: 270px;
    display: flex; justify-content: center; gap: 22px;
    font-family: "Roboto Condensed", sans-serif; font-weight: 700; font-size: 14px;
  }
  .store { display: flex; align-items: center; gap: 6px; }
  .store-dot { width: 10px; height: 10px; border-radius: 50%; background: var(--white); }

  /* Front of card */
  .card-front { top: 493px; height: 342px; background: var(--card-white); }
  .name-tab { position: absolute; left: 0; top: 86px; width: 7px; height: 44px; background: var(--brand-red); }
  .holder-name {
    position: absolute; left: 32px; top: 86px;
    font-family: "Roboto Condensed", sans-serif; font-weight: 700; font-size: 25px; color: var(--brand-red);
  }
  .holder-role {
    position: absolute; left: 32px; top: 113px;
    font-family: "Roboto Condensed", sans-serif; font-weight: 400; font-size: 16px; color: var(--brand-blue);
  }
  .front-crest {
    position: absolute; left: 265px; top: 38px; width: 80px; height: 96px;
    display: flex; align-items: center; justify-content: center;
    font-family: "Roboto Condensed", sans-serif; font-weight: 700; font-size: 20px; color: var(--crest-dark);
  }
  .choir-block { position: absolute; left: 352px; top: 44px; width: 230px; text-align: center; }
  .choir-name { font-family: "Italianno", cursive; font-size: 28px; line-height: 24px; color: var(--brand-red); white-space: nowrap; }
  .choir-minister { font-family: "Roboto Condensed", sans-serif; font-weight: 700; font-size: 14px; color: var(--brand-blue); margin-top: 2px; }
  .choir-church { font-family: "Roboto Condensed", sans-serif; font-size: 11.5px; color: var(--text-grey); margin-top: 5px; line-height: 14px; }
  .front-rule { position: absolute; left: 32px; right: 33px; top: 145px; height: 1px; background: var(--rule-grey); }

  .contact-list {
    position: absolute; left: 34px; top: 215px; list-style: none;
    font-family: "Roboto", sans-serif; font-size: 14.5px; color: var(--text-grey); line-height: 19px;
  }
  .contact-item { display: flex; align-items: center; gap: 8px; }
  .contact-icon { width: 13px; height: 13px; flex: none; }
  .address {
    position: absolute; right: 32px; top: 274px; text-align: right;
    font-family: "Roboto", sans-serif; font-size: 14.5px; color: var(--text-grey); line-height: 19px;
  }
</style>
</head>
<body>
<div class="canvas">

  <section class="card card-back" aria-label="Back of card">
    <div class="back-crest">HVGC</div>
    <p class="back-tagline">Music and Cd's Recordings Available On<br>Choirs Website and Also</p>
    <div class="store-list">
      <span class="store"><span class="store-dot"></span>Tunevox</span>
      <span class="store"><span class="store-dot"></span>Orbala Sound</span>
      <span class="store"><span class="store-dot"></span>Disc Sprout</span>
    </div>
  </section>

  <section class="card card-front" aria-label="Front of card">
    <div class="name-tab"></div>
    <h1 class="holder-name">JORDAN REYES</h1>
    <p class="holder-role">CEO/FOUNDER</p>

    <div class="front-crest">HVGC</div>
    <div class="choir-block">
      <div class="choir-name">The Harlow Vale Gospel Choir</div>
      <div class="choir-minister">Dean Marsell, Minister of Music</div>
      <div class="choir-church">The Coastal Wesleyan Church of Bramford Hill<br>Founded 1792</div>
    </div>
    <div class="front-rule"></div>

    <ul class="contact-list">
      <li class="contact-item"><svg class="contact-icon" viewBox="0 0 13 13"><rect width="13" height="13" rx="2" fill="#c8272e"/></svg>@thehvgc</li>
      <li class="contact-item"><svg class="contact-icon" viewBox="0 0 13 13"><rect width="13" height="13" rx="2" fill="#c8272e"/></svg>harlowvalegc</li>
      <li class="contact-item"><svg class="contact-icon" viewBox="0 0 13 13"><rect width="13" height="13" rx="2" fill="#c8272e"/></svg>/hvgc408</li>
      <li class="contact-item"><svg class="contact-icon" viewBox="0 0 24 24"><path fill="#c8272e" d="M6.6 10.8a15.1 15.1 0 0 0 6.6 6.6l2.2-2.2c.3-.3.7-.4 1-.2 1.1.4 2.3.6 3.6.6.6 0 1 .4 1 1V20c0 .6-.4 1-1 1A17 17 0 0 1 3 4c0-.6.4-1 1-1h3.5c.6 0 1 .4 1 1 0 1.3.2 2.5.6 3.6.1.3 0 .7-.2 1z"/></svg>(555) 204-HVGC (Bookings)</li>
      <li class="contact-item"><svg class="contact-icon" viewBox="0 0 24 24"><circle cx="12" cy="12" r="10" fill="none" stroke="#c8272e" stroke-width="2.4"/><path d="M2 12h20M12 2c3 3 3 17 0 20M12 2c-3 3-3 17 0 20" fill="none" stroke="#c8272e" stroke-width="2"/></svg>www.harlowvalegc-example.org</li>
    </ul>

    <address class="address" style="font-style:normal">4287 Bramwell Street<br>Philadelphia, PA 19874</address>
  </section>

</div>
</body>
</html>
```